Logo-Briefpapier-Visitenkarte für Beratungsunternehmen
Zielgruppe
kleine und Kleinstunternehmer aller Branchen; kleine Unternehmen wie z.B. Friseure, Bäcker, Groß- und Einzelhändler, Handwerker, Floristen, Manufakturen, etc., die Unterstützung und Beratung für ihre Unternehmung wünschen (z.B. Buchhaltung, Jahresabschluss, Steuerberatung, Controlling; Marketing-, Vertriebs-, Organisationsberatung, Prozessgestaltung)
Aufgabenstellung
Erstellung des Designs von Logo, Briefpapier, Visitenkarte(n)
Inhalt Logo: mindestens Namen und Untertitel ("Die Unternehmerpartner")
Inhalt Briefpapier: Logo, Firmenname inkl. Untertitel ("Die Unternehmerpartner"), Kontaktdaten.
Inhalt Visitenkarte: Logo, Firmenname inkl. Untertitel ("Die Unternehmerpartner"), Kontaktdaten inkl. Titel, Berufsbezeichnung, Telefon, email,etc.

```html
<!DOCTYPE html>
<html lang="de">
<head>
<meta charset="utf-8">
<title>Hallberg Norden – Geschäftsausstattung</title>
<link rel="stylesheet" href="https://fonts.googleapis.com/css2?family=Signika:wght@300;400&display=swap">
<style>
  :root {
    --ink: #4a4a4a;
    --ink-soft: #6b6b6b;
    --charcoal: #3c3c3c;
    --card-light: #c9c9c9;
    --gold-dark: #a97a3f;
    --gold-light: #e0be8a;
    --paper: #ffffff;
    --stage: #e8e6e3;
    --sign-blue: #1f3fa3;
  }
  * { box-sizing: border-box; margin: 0; padding: 0; }
  html, body { width: 1200px; height: 1200px; overflow: hidden; }
  body {
    position: relative;
    background: var(--paper);
    font-family: "Signika", sans-serif;
    color: var(--ink);
  }
  .stage {
    position: absolute; left: 0; top: 490px; width: 1200px; height: 710px;
    background: var(--stage);
  }
  .mark-dot {
    display: block; border-radius: 50%;
    background: linear-gradient(135deg, var(--gold-light), var(--gold-dark));
    margin: 0 auto;
  }
  /* Hero logo */
  .hero-logo { position: absolute; left: 0; top: 100px; width: 1200px; text-align: center; }
  .hero-logo .mark-dot { width: 92px; height: 92px; margin-bottom: 52px; }
  .brand-name { font-weight: 300; letter-spacing: 0.5px; line-height: 1; }
  .hero-logo .brand-name { font-size: 72px; color: var(--ink); }
  .tagline { letter-spacing: 2px; font-weight: 400; }
  .hero-logo .tagline { font-size: 19px; margin-top: 18px; color: var(--ink); }

  /* Business card front */
  .card { position: absolute; width: 392px; box-shadow: 0 3px 10px rgba(0,0,0,.22); overflow: hidden; }
  .card-front { left: 131px; top: 584px; height: 253px; background: var(--charcoal); text-align: center; padding-top: 62px; }
  .card-front .mark-dot { width: 48px; height: 48px; margin-bottom: 26px; }
  .card-front .brand-name { font-size: 31px; color: var(--card-light); }
  .card-front .tagline { font-size: 11px; color: var(--ink-soft); margin-top: 8px; letter-spacing: 1.5px; }

  /* Business card back */
  .card-back { left: 131px; top: 861px; height: 275px; background: var(--paper); text-align: center; padding-top: 68px; }
  .card-back .edge { position: absolute; top: 24px; width: 90px; height: 226px; border-radius: 50%;
    background: linear-gradient(180deg, var(--gold-light), var(--gold-dark)); }
  .card-back .edge-left { left: -72px; }
  .card-back .edge-right { right: -72px; }
  .card-back .mark-dot { width: 72px; height: 72px; margin-bottom: 42px; }
  .card-back .contact { font-size: 12.5px; line-height: 17px; color: var(--ink-soft); }
  .card-back .contact .street { margin-bottom: 6px; font-size: 13px; }

  /* Letterhead */
  .letter { position: absolute; left: 581px; top: 432px; width: 483px; height: 680px; background: var(--paper);
    box-shadow: 0 3px 12px rgba(0,0,0,.22); }
  .letter-header { height: 109px; background: var(--charcoal); text-align: center; padding-top: 22px; }
  .letter-header .mark-dot { width: 30px; height: 30px; margin-bottom: 10px; }
  .letter-header .brand-name { font-size: 21px; color: var(--card-light); }
  .letter-header .tagline { font-size: 7px; color: var(--ink-soft); margin-top: 4px; letter-spacing: 1px; }
  .letter-body { position: relative; padding: 22px 55px 0 55px; font-size: 6.4px; line-height: 9px; color: var(--ink); }
  .sender-line { font-size: 5.6px; }
  .recipient { margin-top: 6px; }
  .sender-block { position: absolute; left: 305px; top: 22px; }
  .sender-block .gap { height: 8px; }
  .salutation { margin-top: 92px; }
  .letter-body p { margin-top: 11px; }
  .signature { width: 72px; height: 22px; margin-top: 14px; border-radius: 11px;
    background: linear-gradient(90deg, rgba(31,63,163,.0), rgba(31,63,163,.55), rgba(31,63,163,.0)); }
</style>
</head>
<body>
  <header class="hero-logo">
    <span class="mark-dot"></span>
    <div class="brand-name">Hallberg Norden</div>
    <div class="tagline">Die Unternehmerpartner</div>
  </header>

  <div class="stage"></div>

  <section class="card card-front">
    <span class="mark-dot"></span>
    <div class="brand-name">Hallberg Norden</div>
    <div class="tagline">Die Unternehmerpartner</div>
  </section>

  <section class="card card-back">
    <span class="edge edge-left"></span>
    <span class="edge edge-right"></span>
    <span class="mark-dot"></span>
    <div class="contact">
      <div class="street">Lindenweg 27 | 43210 Auenfeld</div>
      <div>Tel.: +43 (0)30 5550101 | Mobil: +43 (0)170 5550102</div>
      <div>Fax: +43 (0)30 5550103 | E-Mail: kontakt@hallberg-norden.de</div>
    </div>
  </section>

  <section class="letter">
    <div class="letter-header">
      <span class="mark-dot"></span>
      <div class="brand-name">Hallberg Norden</div>
      <div class="tagline">Die Unternehmerpartner</div>
    </div>
    <div class="letter-body">
      <div class="sender-line">Hallberg Norden | Lindenweg 27 | 43210 Auenfeld</div>
      <div class="recipient">Jana Beispiel<br>Musterweg 5<br>12345 Musterstadt</div>
      <div class="sender-block">
        Hallberg Norden<br>Geschäftsführung
        <div class="gap"></div>
        Marktgasse 14<br>1010 Wien
        <div class="gap"></div>
        Tel.: +43 (0)30 5550101<br>Mobil: +43 (0)170 5550102<br>Fax: +43 (0)30 5550103<br>E-Mail: kontakt@hallberg-norden.de
      </div>
      <div class="salutation">Sehr geehrte Damen und Herren,</div>
      <p>gerne begleiten wir Sie bei allen Fragen rund um Ihr Unternehmen. Ob Buchhaltung, Jahresabschluss oder Steuerberatung, wir nehmen uns Zeit für Ihre Anliegen und entwickeln gemeinsam mit Ihnen passende Lösungen. So behalten Sie den Überblick und können sich auf Ihr Kerngeschäft konzentrieren.</p>
      <p>Auch in Marketing, Vertrieb und Organisation stehen wir Ihnen als verlässlicher Partner zur Seite. Wir analysieren Ihre Abläufe, zeigen Potenziale auf und setzen Verbesserungen Schritt für Schritt mit Ihnen um. Dabei zählt für uns jede Idee, ob im Handwerk, im Handel oder in der Manufaktur.</p>
      <p>Gerne vereinbaren wir einen ersten Termin, in dem wir Ihre Ziele besprechen und einen klaren Plan für die kommenden Monate erstellen. Rufen Sie uns einfach an oder schreiben Sie uns eine kurze Nachricht.</p>
      <p>Mit freundlichen Grüßen</p>
      <div class="signature" role="img" aria-label="Handschriftliche Unterschrift in blauer Tinte"></div>
    </div>
  </section>
</body>
</html>
```